Menu Design Project

Hi there!

We're looking to create a kick ass menu for our new restaurant. Our restaurant will be open all day from 10Am till midnight, the kitchen does not close. We will be selling burgers, burritos, pizzas, saladas, cocktails, international beers, sandwiches, wraps.

Our restaurant it's located in Sevilla, Spain. 99% of the restaurants in Sevilla sell tapas & tradional food from Spain but we are sick of that, so we've created this restaurant!

www.lunopage.com/MoraVentaBar

We're targeting all type of people: young travelers, young locals, parents & kids, first time date, you know, everyone!

We will have:

breakfast - Brunch
Lunch & dinner
Happy hour drinks & cocktails
Sandwiches, wraps & pizzas

```html
<!DOCTYPE html>
<html lang="en">
<head>
<meta charset="utf-8">
<title>Mora Venta Bar and Restaurant – Menu</title>
<link rel="stylesheet" href="https://fonts.googleapis.com/css2?family=Kalam:wght@400;700&family=Marcellus+SC&display=swap">
<style>
  :root {
    --backdrop: #e0dcd7;
    --card-white: #ffffff;
    --orange-light: #f6aa43;
    --orange-deep: #f29128;
    --band-red: #e3233a;
    --band-blue: #a6d8ee;
    --ink-brown: #4e3a0b;
    --ink-black: #1c1a17;
  }
  * { margin: 0; padding: 0; box-sizing: border-box; }
  html, body {
    width: 1000px;
    height: 1200px;
    overflow: hidden;
    background: var(--backdrop);
  }
  .menu-card {
    position: absolute;
    left: 220px;
    top: 215px;
    width: 560px;
    height: 768px;
    background: var(--card-white);
    overflow: hidden;
  }
  .card-art {
    position: absolute;
    inset: 0;
    width: 560px;
    height: 768px;
  }
  .brand-name {
    position: absolute;
    left: 0;
    top: 28px;
    width: 520px;
    text-align: center;
    font-family: "Kalam", cursive;
    font-weight: 700;
    font-size: 64px;
    line-height: 1;
    color: var(--ink-black);
  }
  .brand-tagline {
    position: absolute;
    right: 22px;
    top: 118px;
    font-family: "Marcellus SC", serif;
    font-size: 17px;
    letter-spacing: 0.5px;
    color: var(--ink-black);
  }
  .menu-sections {
    position: absolute;
    right: 50px;
    top: 205px;
    list-style: none;
    text-align: right;
    font-family: "Kalam", cursive;
    font-weight: 700;
    font-size: 36px;
    line-height: 52.5px;
    letter-spacing: 1.5px;
    color: var(--ink-brown);
  }
</style>
</head>
<body>
  <main class="menu-card">
    <svg class="card-art" viewBox="0 0 560 768" aria-hidden="false">
      <defs>
        <linearGradient id="orange-field" x1="0" y1="0" x2="1" y2="1">
          <stop offset="0" stop-color="var(--orange-light)"/>
          <stop offset="1" stop-color="var(--orange-deep)"/>
        </linearGradient>
      </defs>
      <path class="band-red" d="M0 285 C 150 215 330 168 545 143 L 545 147 C 340 175 160 225 0 310 Z" fill="var(--band-red)"/>
      <path class="band-blue" d="M0 318 C 160 235 340 182 560 150 L 560 156 C 345 190 170 250 0 332 Z" fill="var(--band-blue)"/>
      <path class="orange-field" role="img" aria-label="Orange brushstroke texture background"
            d="M0 345 C 170 250 350 185 560 153 L 560 768 L 0 768 Z" fill="url(#orange-field)"/>
    </svg>

    <div class="brand-name">Mora Venta</div>
    <div class="brand-tagline">Bar and Restaurant</div>

    <ul class="menu-sections">
      <li>Breakfast</li>
      <li>Sandwiches &amp; Wraps</li>
      <li>Brunch</li>
      <li>Lunch &amp; Dinner</li>
      <li>Deserts</li>
      <li>Happy hours</li>
      <li>International Beers</li>
      <li>Home made Cocktails</li>
      <li>Food to go!</li>
      <li>Milk shakes</li>
    </ul>
  </main>
</body>
</html>
```